Food Hall in San Clemente, CA by the Pacific Ocean that has 15 vendors and 2 bars

We need a web page design that highlights our food hall in San Clemente, CA. The name of the food hall is Tidewell Food Hall. Inside of the food hall there are 15 different vendors and 2 bars. The place has a beautiful patio and it is by Pacific Ocean. Most of the vendors are local to San Clemente area. The highly anticipated location is opening during the summer of 2025. Website should have a dropdown menu for the different vendors that are in the food hall and people should be able to click to their respective business website. The website should also include link to our social media channels and also a link to provide comments and subscribe for the mailing list.
Target Market(s)
Mostly residents in the San Clemente, CA and surrounding areas. Couples, families and tourist alike that are looking for an exceptional dining experience that everyone can find something they like.
Industry/Entity Type
Restaurants
Coding
Coded - Design and coding required
Number of Pages Required
5+ page
Font styles to use
Look and feel
Each slider illustrates characteristics of the customer's brand and the style your logo design should communicate.

```html
<!DOCTYPE html>
<html lang="en">
<head>
<meta charset="UTF-8">
<title>Tidewell Food Hall</title>
<link href="https://fonts.googleapis.com/css2?family=Open+Sans:wght@400;600;700&display=swap" rel="stylesheet">
<style>
  :root {
    --ocean-deep: #0a56a8;
    --ocean-bright: #0893d3;
    --hero-top: #7fb6dc;
    --hero-bottom: #d8d6cf;
    --card-white: #ffffff;
    --field-border: #4d8fc6;
    --text-muted: #666666;
    --text-light: #ffffff;
  }
  * { box-sizing: border-box; margin: 0; padding: 0; }
  html, body {
    width: 815px;
    height: 1200px;
    overflow: hidden;
    font-family: "Open Sans", Arial, sans-serif;
    background: var(--ocean-deep);
  }
  .page { width: 815px; height: 1200px; display: flex; flex-direction: column; }

  .hero {
    position: relative;
    height: 333px;
    flex-shrink: 0;
  }
  .hero-backdrop {
    position: absolute;
    inset: 0;
    background: linear-gradient(180deg, var(--hero-top) 0%, var(--hero-bottom) 100%);
  }
  .hero-content {
    position: relative;
    height: 100%;
    display: flex;
    flex-direction: column;
    align-items: center;
    justify-content: center;
    text-align: center;
    color: var(--text-light);
    padding: 0 20px 50px;
  }
  .hero-title {
    font-size: 32px;
    font-weight: 700;
    margin-bottom: 10px;
    text-shadow: 0 2px 6px rgba(0,0,0,0.35);
  }
  .hero-tagline {
    font-size: 20px;
    line-height: 1.3;
    text-shadow: 0 1px 4px rgba(0,0,0,0.35);
  }

  .vendor-menu {
    position: absolute;
    top: 16px;
    right: 20px;
    z-index: 2;
  }
  .vendor-menu summary {
    list-style: none;
    cursor: pointer;
    background: var(--ocean-deep);
    color: var(--text-light);
    font-size: 15px;
    font-weight: 600;
    padding: 7px 16px;
    border-radius: 6px;
    display: flex;
    align-items: center;
    gap: 8px;
  }
  .vendor-menu summary::-webkit-details-marker { display: none; }

  .signup {
    background: var(--ocean-deep);
    padding: 36px 4px 53px;
  }
  .signup-card {
    background: var(--card-white);
    border-radius: 18px;
    padding: 76px 39px 53px;
    text-align: center;
  }
  .signup-title {
    color: var(--ocean-deep);
    font-size: 26px;
    font-weight: 700;
    line-height: 36px;
    margin-bottom: 21px;
  }
  .signup-field {
    display: block;
    width: 100%;
    border: 1.5px solid var(--field-border);
    border-radius: 7px;
    font-size: 15px;
    color: var(--text-muted);
    text-align: left;
    padding: 0 18px;
    background: var(--card-white);
  }
  .signup-field.email { height: 60px; line-height: 57px; margin-bottom: 29px; }
  .signup-field.comment { height: 109px; padding-top: 14px; line-height: 1.3; margin-bottom: 26px; }
  .signup-button {
    display: block;
    width: 100%;
    height: 58px;
    border: none;
    border-radius: 7px;
    background: var(--ocean-bright);
    color: var(--text-light);
    font-family: inherit;
    font-size: 18px;
    font-weight: 700;
  }

  .site-footer {
    flex: 1;
    background: var(--ocean-bright);
    color: var(--text-light);
    text-align: center;
    padding-top: 45px;
  }
  .footer-copy { font-size: 17px; line-height: 24px; margin-bottom: 16px; }
  .footer-links { display: flex; justify-content: center; gap: 40px; }
  .footer-links a { color: var(--text-light); text-decoration: none; font-size: 17px; font-weight: 700; }
</style>
</head>
<body>
<div class="page">
  <header class="hero">
    <div class="hero-backdrop" role="img" aria-label="Photo of a sunny beach with palm trees and umbrellas by the ocean"></div>
    <details class="vendor-menu">
      <summary>Vendors
        <svg width="12" height="8" viewBox="0 0 12 8" aria-hidden="true"><path d="M1 1l5 5 5-5" fill="none" stroke="#ffffff" stroke-width="2"/></svg>
      </summary>
    </details>
    <div class="hero-content">
      <h1 class="hero-title">Welcome to Tidewell Food Hall</h1>
      <p class="hero-tagline">Opening Summer 2025 - Located on the beautiful terrace by the Pacific Ocean in San Clemente</p>
    </div>
  </header>

  <section class="signup">
    <div class="signup-card">
      <h2 class="signup-title">Stay in Touch</h2>
      <div class="signup-field email">Enter your email</div>
      <div class="signup-field comment">Leave a comment...</div>
      <button class="signup-button" type="button">Subscribe</button>
    </div>
  </section>

  <footer class="site-footer">
    <p class="footer-copy">© 2025 Tidewell Food Hall</p>
    <nav class="footer-links">
      <a href="#">Snapgrid</a>
      <a href="#">Friendbook</a>
      <a href="#">Chirper</a>
    </nav>
  </footer>
</div>
</body>
</html>
```